Civic Learning Workshop Pocketdeck

We are looking for a fresh new look for our famous Signal Sense Pocketdeck cards. These cards are used as a pedagogical device by teachers and students to help people critically analyze media messages.

Now that we are in the era of Veltro 9, we would like the Signal Sense Pocketdeck to look fresh and new. All the content stays the same, but graphic elements, color and overall design can be changed to look contemporary and modern.

Target Market(s)

Teenagers, young adults, secondary and college teachers

Industry/Entity Type

Education

Colors

Designer to choose colors to be used in the design.

Requirements
Must have
• All the content that is on the current card, with icons and text
Nice to have
• Fresh use of color
• More modern phone design like the smartphones people use today
Should not have
• ...too much black

```html
<!DOCTYPE html>
<html lang="en">
<head>
<meta charset="utf-8">
<title>Signal Sense Pocketdeck – Time to Discuss</title>
<link rel="stylesheet" href="https://fonts.googleapis.com/css2?family=Arimo:wght@400;700&display=swap">
<style>
  :root {
    --orange: #f15a29;
    --teal: #1fa3b5;
    --green: #8cc63f;
    --yellow: #fbb03b;
    --red: #ef4136;
    --frame: #1c1c1e;
    --frame-edge: #8a8a8a;
    --screen: #ffffff;
    --tray: #ededed;
    --ink: #222222;
    --canvas: #ffffff;
  }
  * { box-sizing: border-box; margin: 0; padding: 0; }
  html, body { width: 929px; height: 1200px; overflow: hidden; background: var(--canvas); }
  body { position: relative; font-family: "Arimo", Arial, sans-serif; color: var(--ink); }

  .phone {
    position: absolute; left: 178px; top: 18px; width: 574px; height: 1166px;
    background: var(--frame); border: 4px solid var(--frame-edge); border-radius: 92px;
  }
  .screen {
    position: absolute; left: 22px; top: 22px; right: 22px; bottom: 22px;
    background: var(--screen); border-radius: 68px; overflow: hidden;
    display: flex; flex-direction: column;
  }
  .notch {
    position: absolute; left: 50%; top: 0; width: 230px; height: 50px; transform: translateX(-50%);
    background: var(--frame); border-radius: 0 0 28px 28px; z-index: 2;
  }
  .notch::after {
    content: ""; position: absolute; left: 150px; top: 14px; width: 16px; height: 16px;
    border-radius: 50%; background: #3b4d6b;
  }
  .header-band { height: 160px; background: var(--orange); flex: none; }

  .title-block { margin: 22px 26px 0; text-align: center; flex: none; }
  .title-rule { height: 9px; border-top: 3px solid var(--orange); border-bottom: 2px solid var(--orange); }
  .title {
    color: var(--orange); font-weight: 700; font-size: 38px; letter-spacing: 1px;
    padding: 8px 0 6px;
  }

  .prompt-grid {
    display: grid; grid-template-columns: repeat(4, 1fr); row-gap: 22px;
    padding: 26px 30px 0; flex: none;
  }
  .prompt { text-align: center; font-size: 21px; line-height: 1.12; }
  .prompt-icon {
    width: 66px; height: 66px; margin: 0 auto 6px; border-radius: 12px;
    display: flex; align-items: center; justify-content: center;
  }
  .prompt-icon svg { width: 42px; height: 42px; }
  .teal { background: var(--teal); }
  .green { background: var(--green); }
  .yellow { background: var(--yellow); }
  .red { background: var(--red); }

  .media-tray {
    flex: 1; margin-top: 24px; background: var(--tray);
    display: grid; grid-template-columns: repeat(4, 1fr); align-content: start; row-gap: 26px;
    padding: 30px 30px 0;
  }
  .medium { text-align: center; font-size: 21px; line-height: 1.12; }
  .medium-icon {
    width: 64px; height: 64px; margin: 0 auto 6px; background: #fff; border-radius: 14px;
    display: flex; align-items: center; justify-content: center;
  }
  .medium-icon svg { width: 42px; height: 42px; }
</style>
</head>
<body>
<div class="phone">
  <div class="screen">
    <div class="notch"></div>
    <div class="header-band"></div>

    <div class="title-block">
      <div class="title-rule"></div>
      <h1 class="title">TIME TO DISCUSS</h1>
      <div class="title-rule"></div>
    </div>

    <div class="prompt-grid">
      <div class="prompt">
        <div class="prompt-icon teal"><svg viewBox="0 0 40 40"><path d="M8 21 L16 29 L32 11" fill="none" stroke="#fff" stroke-width="6" stroke-linecap="round" stroke-linejoin="round"/></svg></div>
        Reality Check
      </div>
      <div class="prompt">
        <div class="prompt-icon green"><svg viewBox="0 0 40 40"><path d="M14 6 H26 L23 12 H17 Z" fill="#fff"/><path d="M17 13 H23 C32 18 34 34 20 35 C6 34 8 18 17 13 Z" fill="#fff"/><text x="20" y="31" text-anchor="middle" font-family="Arimo, Arial, sans-serif" font-weight="700" font-size="15" fill="#8cc63f">$</text></svg></div>
        Private Gain or Public Good?
      </div>
      <div class="prompt">
        <div class="prompt-icon yellow"><svg viewBox="0 0 40 40"><text x="20" y="33" text-anchor="middle" font-family="Arimo, Arial, sans-serif" font-weight="700" font-size="34" fill="#fff">?</text></svg></div>
        What's Left Out?
      </div>
      <div class="prompt">
        <div class="prompt-icon red"><svg viewBox="0 0 40 40"><path d="M11 8 H29 L36 16 L20 34 L4 16 Z M4 16 H36 M14 8 L20 16 L26 8 M13 16 L20 34 L27 16" fill="none" stroke="#fff" stroke-width="2.6" stroke-linejoin="round"/></svg></div>
        Values Check
      </div>

      <div class="prompt">
        <div class="prompt-icon red"><svg viewBox="0 0 40 40"><path d="M3 20 C10 9 30 9 37 20 C30 31 10 31 3 20 Z" fill="#fff"/><circle cx="20" cy="20" r="7" fill="#ef4136"/><circle cx="20" cy="20" r="3" fill="#fff"/></svg></div>
        Read Between the Lines
      </div>
      <div class="prompt">
        <div class="prompt-icon yellow"><svg viewBox="0 0 40 40"><path d="M20 5 C12 5 10 12 10 18 V26 L6 30 H34 L30 26 V18 C30 12 28 5 20 5 Z" fill="#fff"/><circle cx="20" cy="34" r="4" fill="#fff"/></svg></div>
        Stereotype Alert
      </div>
      <div class="prompt">
        <div class="prompt-icon green"><svg viewBox="0 0 40 40"><path d="M20 4 L37 35 H3 Z" fill="#fff"/><rect x="18" y="14" width="4" height="12" fill="#8cc63f"/><rect x="18" y="28" width="4" height="4" fill="#8cc63f"/></svg></div>
        Solutions too Easy
      </div>
      <div class="prompt">
        <div class="prompt-icon teal"><svg viewBox="0 0 40 40"><path d="M8 28 L26 10 L31 15 L13 33 H8 Z" fill="#fff"/><path d="M28 8 L31 5 L36 10 L33 13 Z" fill="#fff"/><rect x="6" y="35" width="28" height="2.5" fill="#fff"/></svg></div>
        Record/ Save for Later
      </div>
    </div>

    <div class="media-tray">
      <div class="medium">
        <div class="medium-icon"><svg viewBox="0 0 40 40"><rect x="4" y="8" width="32" height="25" rx="2" fill="none" stroke="#222" stroke-width="3"/><rect x="9" y="13" width="10" height="8" fill="#222"/><path d="M22 14 H31 M22 19 H31 M9 25 H31 M9 29 H25" stroke="#222" stroke-width="2.5"/></svg></div>
        News Media
      </div>
      <div class="medium">
        <div class="medium-icon"><svg viewBox="0 0 40 40"><circle cx="20" cy="20" r="15" fill="#222"/><path d="M5 20 H35 M20 5 V35 M10 9 C16 16 16 24 10 31 M30 9 C24 16 24 24 30 31" fill="none" stroke="#fff" stroke-width="2"/></svg></div>
        Websites
      </div>
      <div class="medium">
        <div class="medium-icon"><svg viewBox="0 0 40 40"><path d="M13 4 L20 12 L27 4" fill="none" stroke="#222" stroke-width="2.5"/><rect x="4" y="12" width="32" height="22" rx="2" fill="none" stroke="#222" stroke-width="3"/><rect x="14" y="35" width="12" height="3" fill="#222"/></svg></div>
        TV
      </div>
      <div class="medium">
        <div class="medium-icon"><svg viewBox="0 0 40 40"><rect x="5" y="16" width="30" height="19" fill="#222"/><path d="M5 8 L33 3 L34 10 L6 15 Z" fill="#222"/><path d="M12 7 L15 13 M20 6 L23 12 M28 4 L31 10" stroke="#fff" stroke-width="2"/></svg></div>
        Movies
      </div>

      <div class="medium">
        <div class="medium-icon"><svg viewBox="0 0 40 40"><rect x="10" y="4" width="20" height="32" rx="3" fill="#222"/><rect x="13" y="8" width="14" height="22" fill="#fff"/></svg></div>
        Apps
      </div>
      <div class="medium">
        <div class="medium-icon"><svg viewBox="0 0 40 40"><path d="M10 14 L28 6" stroke="#222" stroke-width="2.5"/><rect x="4" y="14" width="32" height="22" rx="2" fill="#222"/><circle cx="14" cy="25" r="6" fill="#fff"/><rect x="23" y="19" width="9" height="3" fill="#fff"/><rect x="23" y="25" width="9" height="3" fill="#fff"/></svg></div>
        Podcasts
      </div>
      <div class="medium">
        <div class="medium-icon"><svg viewBox="0 0 40 40"><path d="M4 6 H36 V28 H16 L8 35 V28 H4 Z" fill="#222"/><circle cx="13" cy="17" r="2.5" fill="#fff"/><circle cx="20" cy="17" r="2.5" fill="#fff"/><circle cx="27" cy="17" r="2.5" fill="#fff"/></svg></div>
        Comics
      </div>
      <div class="medium">
        <div class="medium-icon"><svg viewBox="0 0 40 40"><rect x="8" y="4" width="24" height="32" rx="2" fill="#222"/><rect x="8" y="31" width="24" height="3" fill="#fff"/></svg></div>
        Books
      </div>

      <div class="medium">
        <div class="medium-icon"><svg viewBox="0 0 40 40"><path d="M14 8 L32 4 V27" fill="none" stroke="#222" stroke-width="3.5"/><path d="M14 8 V31" stroke="#222" stroke-width="3.5"/><ellipse cx="10" cy="31" rx="6" ry="4.5" fill="#222"/><ellipse cx="28" cy="27" rx="6" ry="4.5" fill="#222"/></svg></div>
        Music
      </div>
      <div class="medium">
        <div class="medium-icon"><svg viewBox="0 0 40 40"><path d="M29 9 L11 20 L29 31" fill="none" stroke="#222" stroke-width="3"/><circle cx="29" cy="9" r="6" fill="#222"/><circle cx="11" cy="20" r="6" fill="#222"/><circle cx="29" cy="31" r="6" fill="#222"/></svg></div>
        Social Media
      </div>
      <div class="medium">
        <div class="medium-icon"><svg viewBox="0 0 40 40"><path d="M11 11 H29 C35 11 38 20 38 27 C38 32 33 33 30 28 L27 24 H13 L10 28 C7 33 2 32 2 27 C2 20 5 11 11 11 Z" fill="#222"/><path d="M11 15 V21 M8 18 H14" stroke="#fff" stroke-width="2.2"/><circle cx="27" cy="16" r="1.8" fill="#fff"/><circle cx="31" cy="20" r="1.8" fill="#fff"/></svg></div>
        Video Games
      </div>
      <div class="medium">
        <div class="medium-icon"><svg viewBox="0 0 40 40"><path d="M13 10 A13 13 0 1 0 27 10" fill="none" stroke="#222" stroke-width="4" stroke-linecap="round"/><path d="M20 4 V20" stroke="#222" stroke-width="4" stroke-linecap="round"/></svg></div>
        Off
      </div>
    </div>
  </div>
</div>
</body>
</html>
```